Veteran Owned General Contractor needs Bold New Business Cards

We are a service disabled veteran owned small business. We're a general contractor that specializes in excavation, underground utilities, site work, land clearing and demolition. We would like a fresh, simple, bold, new look for our business cards. We're open to ideas! We'd like to incorporate the following information on the card:

Company Name & Logo, Name of Person, Job Title, Office Phone, Fax, Cell Phone, Email Address, Website, SDVOSB

Our logo is included. We look forward to your thoughts.

Thank you!
Updates

Reason: Hello Due to the overwhelming response to this project, we are extending the deadline one time to allow for improved communication and feedback with the top candidates. We would like to thank everyone for their hard work and exceptional creativity! Thank you

Industry/Entity Type

Business

Contact Information for Business Card

Font styles to use
Sans Serif

Requirements
Nice to have
• As we are a veteran owned company, it would be nice to incorporate an American flag into the design. Maybe on the back?

```html
<!DOCTYPE html>
<html lang="en">
<head>
<meta charset="utf-8">
<title>Summit4 Inc Business Cards</title>
<link rel="stylesheet" href="https://fonts.googleapis.com/css2?family=Open+Sans:wght@400;700&display=swap">
<style>
  :root {
    --page: #e9ecef;
    --card-dark: #232833;
    --card-light: #ffffff;
    --brand-green: #6cbd45;
    --name-grey: #c9ccd1;
    --label-grey: #5f6368;
    --flag-tone: #e6e7e9;
    --flag-tone-2: #d9dadd;
  }
  html, body {
    margin: 0;
    padding: 0;
    width: 1200px;
    height: 1000px;
    overflow: hidden;
    background: var(--page);
    font-family: "Open Sans", sans-serif;
  }
  .canvas {
    position: relative;
    width: 1200px;
    height: 1000px;
  }
  .card {
    position: absolute;
    box-shadow: 0 4px 14px rgba(0,0,0,0.12);
    overflow: hidden;
  }
  .card-front {
    left: 162px;
    top: 34px;
    width: 658px;
    height: 406px;
    background: var(--card-dark);
    display: flex;
    align-items: center;
    justify-content: center;
  }
  .brand {
    display: flex;
    align-items: center;
    gap: 26px;
  }
  .brand-square {
    width: 70px;
    height: 70px;
    background: var(--brand-green);
  }
  .brand-name {
    font-weight: 700;
    font-size: 72px;
    letter-spacing: 2px;
    color: var(--brand-green);
    line-height: 1;
  }
  .card-back {
    left: 367px;
    top: 532px;
    width: 668px;
    height: 401px;
    background: var(--card-light);
  }
  .identity-band {
    height: 200px;
    background: var(--card-dark);
    text-align: center;
    color: var(--name-grey);
  }
  .person-name {
    padding-top: 72px;
    margin: 0;
    font-weight: 400;
    font-size: 28px;
    letter-spacing: 14px;
    line-height: 36px;
  }
  .job-title {
    margin: 8px 0 0;
    font-size: 17px;
    line-height: 24px;
  }
  .company-tag {
    margin: 14px 0 0;
    font-size: 17px;
    line-height: 24px;
    letter-spacing: 0.5px;
  }
  .contact-list {
    position: absolute;
    left: 0;
    top: 231px;
    width: 190px;
    margin: 0;
    padding: 0;
    list-style: none;
    text-align: right;
    font-size: 17px;
    line-height: 24px;
    color: var(--label-grey);
  }
  .flag-art {
    position: absolute;
    left: 310px;
    top: 208px;
    width: 310px;
    height: 180px;
    border-radius: 18px 30px 14px 40px;
    background: linear-gradient(160deg, var(--flag-tone-2), var(--flag-tone));
    transform: rotate(8deg);
  }
</style>
</head>
<body>
  <main class="canvas">
    <section class="card card-front" aria-label="Card front">
      <div class="brand">
        <div class="brand-square"></div>
        <span class="brand-name">SUMMIT4 INC</span>
      </div>
    </section>

    <section class="card card-back" aria-label="Card back">
      <header class="identity-band">
        <h1 class="person-name">Name of Person</h1>
        <p class="job-title">Job Title</p>
        <p class="company-tag">( SUMMIT 4 )</p>
      </header>
      <ul class="contact-list">
        <li>Office Phone :</li>
        <li>Fax :</li>
        <li>Cell Phone :</li>
        <li>Email Address :</li>
        <li>Website :</li>
      </ul>
      <div class="flag-art" role="img" aria-label="Faint grey waving American flag illustration"></div>
    </section>
  </main>
</body>
</html>
```